B2B Software Company Needs 300x250 banner ad

I need a 300x250 static gif banner ad for a web site/online newsletter that we advertise on. We're a B2B software company, and the audience for this banner ad is medical device development team leads and managers. We would like to see designs that use blue (mainly), accent colors of orange, bright green, and purple are OK, too. This is a text heavy add but that can't be changed. I'm attaching our corporate logo, the copy file (Harbor Ledger.doc), latest version of our style guide, and an example of a previous ad we've done (which we don't necessarily need to/want to recreate). We want something that is pleasing to look at, easy to read, and gets someone to click through to the landing page.

Industry/Entity Type

Software

Requirements
Should not have
• Please do not re-lay out the 2013 outlook of Clinical Hardware Engineering banner. That was simply uploaded as an example. The docx Word document/copy should be used for a new banner ad.

```html
<!DOCTYPE html>
<html lang="en">
<head>
<meta charset="utf-8">
<title>Exclusive White Paper Banner</title>
<link href="https://fonts.googleapis.com/css2?family=Arimo:wght@400;700&display=swap" rel="stylesheet">
<style>
  :root {
    --page-bg: #e6e7e8;
    --banner-blue: #0a7bc4;
    --banner-border: #0a0a0a;
    --headline-white: #ffffff;
    --accent-green: #8cc63f;
    --body-ink: #0b0b0b;
    --footer-black: #000000;
    --callout-shadow: rgba(0, 0, 0, 0.45);
  }
  * { margin: 0; padding: 0; box-sizing: border-box; }
  html, body {
    width: 1200px;
    height: 900px;
    overflow: hidden;
    background: var(--page-bg);
    font-family: "Arimo", Arial, sans-serif;
  }
  .banner {
    position: absolute;
    left: 375px;
    top: 262px;
    width: 450px;
    height: 375px;
    background: var(--banner-blue);
    border: 1.5px solid var(--banner-border);
    overflow: hidden;
  }
  .banner-kicker {
    position: absolute;
    top: 22px;
    left: 0;
    width: 100%;
    text-align: center;
    color: var(--headline-white);
    font-weight: 700;
    font-size: 28px;
    letter-spacing: 0.5px;
    line-height: 36px;
  }
  .paper-title {
    position: absolute;
    left: 16px;
    top: 72px;
    width: 418px;
    height: 78px;
    background: var(--headline-white);
    box-shadow: 5px 5px 6px var(--callout-shadow);
    padding: 3px 0 0 14px;
    color: var(--accent-green);
    font-weight: 700;
    font-size: 25.5px;
    letter-spacing: 0.6px;
    line-height: 36px;
  }
  .banner-copy {
    position: absolute;
    left: 27px;
    top: 165px;
    width: 400px;
    color: var(--body-ink);
    font-weight: 700;
    font-size: 21px;
    letter-spacing: 0.2px;
    line-height: 34.5px;
  }
  .banner-footer {
    position: absolute;
    left: 0;
    bottom: 0;
    width: 100%;
    height: 58px;
    background: var(--footer-black);
    display: flex;
    align-items: center;
    justify-content: flex-end;
    padding-right: 16px;
    gap: 8px;
  }
  .brand-mark {
    width: 14px;
    height: 14px;
    background: var(--headline-white);
  }
  .brand-name {
    color: var(--headline-white);
    font-weight: 400;
    font-size: 23px;
    letter-spacing: -0.3px;
  }
</style>
</head>
<body>
  <div class="banner">
    <p class="banner-kicker">Exclusive White Paper:</p>
    <h1 class="paper-title">Exposing Risk In Product<br>Development Lifecycles</h1>
    <p class="banner-copy">Reduce time spent managing risk and support regulatory approvals with traceability-based risk management.</p>
    <div class="banner-footer">
      <span class="brand-mark"></span>
      <span class="brand-name">Tidewell Software</span>
    </div>
  </div>
</body>
</html>
```